Re-Design of a 1 Pager IT Security Website

Please create a 1 Pager design for this website and all its elements: http://www.vantorelgrid.com/

Colours, Fonts etc: You can select whatever you prefer

```html
<!DOCTYPE html>
<html lang="en">
<head>
<meta charset="utf-8">
<title>Domain Monitoring – Veltrana</title>
<link href="https://fonts.googleapis.com/css2?family=Montserrat:wght@400;500;600;700;800;900&display=swap" rel="stylesheet">
<style>
:root{
  --blue:#0a4c9c;
  --blue-deep:#0b3f86;
  --navy:#0c2550;
  --navy-dark:#07193a;
  --cyan:#00d2f5;
  --cyan-soft:#4fd2f0;
  --ink:#333c48;
  --muted:#5a6270;
  --white:#ffffff;
  --line:#0a4c9c;
  --pale:#e4f1fb;
}
*{box-sizing:border-box;margin:0;padding:0}
html,body{width:1200px;height:3858px;overflow:hidden;background:var(--white)}
body{position:relative;font-family:'Montserrat',sans-serif;color:var(--ink)}
.abs{position:absolute}

/* hero */
.hero{left:0;top:0;width:1200px;height:680px;background:radial-gradient(ellipse at 45% 45%,#2a8ae0 0%,#0b4fa8 35%,#072f6e 70%,#041c45 100%)}
.brand{left:132px;top:28px;font-weight:800;font-size:22px;color:var(--white);letter-spacing:.3px}
.nav{top:32px;font-weight:700;font-size:14px;color:var(--white)}
.nav.active{padding-bottom:6px;border-bottom:2px solid var(--white)}
.hero-title{left:742px;top:216px;font-weight:900;font-size:34px;line-height:40px;color:var(--white)}
.btn-light{left:744px;top:360px;width:129px;height:39px;background:var(--white);color:var(--navy);font-weight:800;font-size:15px;display:flex;align-items:center;justify-content:center}

/* section titles */
.h2{font-weight:800;font-size:22px;color:var(--blue)}
.h2.light{color:var(--white)}
.rule{height:2px;width:70px;background:var(--blue)}
.rule.light{background:var(--white)}
.body{font-size:13.5px;line-height:20.7px;color:var(--muted);text-align:justify}

/* risk */
.risk-visual{left:132px;top:727px;width:517px;height:329px;background:radial-gradient(circle at 50% 50%,#1d6fb8 0%,#0e3e73 38%,#d7ecfa 39%,#e4f1fb 100%)}
.card{width:292px;height:404px;background:var(--white);box-shadow:0 6px 24px rgba(20,40,80,.12);text-align:center;padding:0 36px}
.card.featured{background:var(--blue);color:var(--white)}
.card svg{margin-top:36px}
.card h3{font-weight:700;font-size:16px;color:var(--blue);margin-top:16px}
.card.featured h3{color:var(--white)}
.card p{font-size:12px;line-height:16px;color:var(--muted);margin-top:14px}
.card.featured p{color:var(--white)}

/* protect */
.protect{left:0;top:1562px;width:1200px;height:502px;background:var(--navy)}
.protect-visual{left:510px;top:1562px;width:690px;height:502px;background:linear-gradient(90deg,var(--navy) 0%,#1b4f93 30%,#3b7fc4 60%,#1c4e8f 100%)}
.protect p{font-size:14.5px;line-height:21px;color:var(--white)}
.protect a{color:var(--white)}

/* monitoring */
.monitor-bg{left:0;top:2064px;width:560px;height:648px;background:linear-gradient(180deg,#e7eff6,#dde8f1)}
.monitor-visual{left:135px;top:2118px;width:506px;height:532px;background:linear-gradient(160deg,#5fb4e8 0%,#2d7ac0 50%,#123f7a 100%)}
.feature{left:688px;width:379px;height:64px;display:flex;align-items:center;padding-left:20px;color:var(--white)}
.feature svg{flex:none}
.feature .txt{margin-left:24px;font-size:13px;line-height:18px}
.feature b{font-weight:800}

/* about */
.about{left:0;top:2712px;width:1200px;height:344px;background:linear-gradient(180deg,#0a1f3c 0%,#102d52 60%,#0b2244 100%)}
.about p{font-size:18px;line-height:23.5px;color:var(--white);text-align:center;font-weight:500}

/* contact */
.contact{left:0;top:3056px;width:1200px;height:514px;background:linear-gradient(180deg,#0b4fa8 0%,#0a46a0 100%)}
.panel{left:303px;top:3186px;width:593px;height:384px;background:var(--white)}
.field{border:1px solid var(--blue);font-size:12px;color:var(--muted);padding:12px 16px}
.submit{left:550px;top:3489px;width:100px;height:36px;background:var(--blue);color:var(--white);font-weight:800;font-size:14px;display:flex;align-items:center;justify-content:center}

/* footer */
.foot-brand{left:0;width:1200px;top:3622px;text-align:center;font-weight:800;font-size:26px;color:var(--blue)}
.foot-nav{left:371px;top:3685px;height:35px;display:flex;border:1px solid var(--blue)}
.foot-nav span{display:flex;align-items:center;justify-content:center;font-size:14px;color:var(--ink);border-right:1px solid var(--blue)}
.foot-nav span:last-child{border-right:none}
.follow{left:523px;top:3754px;font-size:11px;color:var(--ink);display:flex;align-items:center;gap:10px}
.dot{width:26px;height:26px;border-radius:50%;background:var(--blue)}
.dot.alt{background:#1e9be0}
.copy{left:0;width:1200px;top:3811px;text-align:center;font-size:12px;color:var(--muted)}
</style>
</head>
<body>

<!-- hero -->
<section class="abs hero" role="img" aria-label="Glowing blue backdrop of domain endings such as .com, .net, .org and www floating in digital space"></section>
<div class="abs brand">DOMAIN MONITORING</div>
<div class="abs nav active" style="left:682px">HOME</div>
<div class="abs nav" style="left:757px">ABOUT US</div>
<div class="abs nav" style="left:869px">PROTECT</div>
<div class="abs nav" style="left:971px">CONTACT US</div>
<h1 class="abs hero-title">PREVENT ATTACKS<br>BY MONITORING<br>YOUR DOMAINS</h1>
<div class="abs btn-light">LEARN MORE</div>

<!-- risk -->
<div class="abs risk-visual" role="img" aria-label="Digital globe of binary code with a browser address bar and search field across it"></div>
<h2 class="abs h2" style="left:715px;top:738px">WHAT IS THE RISK?</h2>
<div class="abs rule" style="left:715px;top:775px"></div>
<p class="abs body" style="left:715px;top:807px;width:350px">Hackers use domain-based attacks, which are designed to trick users into submitting sensitive data or downloading dangerous files. This is often the case with phishing attacks. For example, domains can be registered that are very similar to one's own company, a customer or a supplier. Once a fraudulent domain is registered, the hackers try to lure the employee to the website. This can be done via e-mail, SMS (smishing), instant messaging. Social media and many other techniques succeed. A distinction is made between different types of attacks:</p>

<div class="abs card" style="left:133px;top:1104px">
  <svg width="68" height="64" viewBox="0 0 68 64" fill="none" stroke="#0a4c9c" stroke-width="2"><rect x="4" y="4" width="46" height="42" rx="2"/><line x1="4" y1="12" x2="50" y2="12"/><circle cx="30" cy="34" r="14"/><line x1="40" y1="44" x2="56" y2="60"/><text x="20" y="38" font-size="10" font-family="Montserrat" fill="#0a4c9c" stroke="none">.com</text></svg>
  <h3>Domain Spoofing</h3>
  <p>Here, a domain name is registered that resembles that of a trusted brand or organization. For example, the hacker can register the domain "paybridge - access .services" and lure the victim to the website under a certain pretext. At the same time, the original website can also be copied 1:1, so that visually there is no difference.</p>
</div>
<div class="abs card featured" style="left:454px;top:1104px">
  <svg width="68" height="64" viewBox="0 0 68 64" fill="none" stroke="#ffffff" stroke-width="2"><rect x="8" y="4" width="40" height="46" rx="2"/><line x1="8" y1="14" x2="48" y2="14"/><circle cx="40" cy="40" r="13"/><line x1="49" y1="49" x2="62" y2="62"/><circle cx="40" cy="40" r="5"/></svg>
  <h3>Homoglyphic attack</h3>
  <p>This is a variant of domain spoofing. Again, a similar looking domain is registered. But one uses characters outside the Latin alphabet in the domain name that resemble the corresponding characters in the URL of the target domain. Replacing the "g" with q is also very popular. Multi-letter homoglyphs are also popular, e.g. "rn" instead of "m". In more complex scenarios, homoglyphs can also be generated with the use of different alphabets and special characters.</p>
</div>
<div class="abs card" style="left:773px;top:1104px">
  <svg width="68" height="64" viewBox="0 0 68 64" fill="none" stroke="#0a4c9c" stroke-width="2"><rect x="8" y="8" width="34" height="46" rx="2"/><circle cx="36" cy="22" r="10"/><line x1="30" y1="36" x2="60" y2="36"/><line x1="30" y1="44" x2="60" y2="44"/><line x1="30" y1="52" x2="60" y2="52"/></svg>
  <h3>Typosquatting</h3>
  <p>Cybercriminals may attempt to register a malicious domain by using a common misspelling of the target company's domain. For example, someone might reserve "paybridhe.com" because the letter "G" and "H" are next to each other at the keyboard. If a customer of the target company misspells the domain, he will land on the fraudulent domain where he can become a victim of cybercriminals.</p>
</div>

<!-- protect -->
<section class="abs protect">
  <div class="abs protect-visual" style="top:0" role="img" aria-label="Hand touching a glowing .com hexagon among other domain endings"></div>
  <h2 class="abs h2 light" style="left:135px;top:70px;line-height:32px">HOW TO PROTECT<br>YOURSELF?</h2>
  <div class="abs rule light" style="left:135px;top:150px;width:122px"></div>
  <p class="abs" style="left:135px;top:184px;width:310px">Our domain monitoring solution continuously monitors thousands of TLDs, gTLDs and ccTLDs. For searches, we offer the greatest flexibility in the market and cover ALL forms of attacks. Here are a few examples of search options that can be adopted as active alerts: <a href="#">https://docs.veltrana.io/guide/domain_database_search.</a></p>
  <p class="abs" style="left:135px;top:390px">All data can be analyzed and exported.</p>
</section>

<!-- monitoring -->
<div class="abs monitor-bg"></div>
<div class="abs monitor-visual" role="img" aria-label="Hand holding a magnifying glass over a glowing domain globe icon on a data screen"></div>
<h2 class="abs h2" style="left:683px;top:2115px">WHAT ELSE ARE WE MONITORING?</h2>
<p class="abs body" style="left:685px;top:2181px;width:382px">Veltrana helps you understand when, where and how stolen or accidentally leaked information in dark web markets, forums, botnet logs, IRC, social media and other sources is exposed. Veltrana's alerting service can also detect threats before they turn into incidents. Veltrana offers AI-driven dark web analysis, real-time threat alerts and pre-Attack threat indicators. Setup in minutes you will receive instant access to real-time reporting including:</p>

<div class="abs feature" style="top:2373px;background:#00d0f4"><svg width="44" height="44" viewBox="0 0 44 44" fill="none" stroke="#fff" stroke-width="1.6"><circle cx="22" cy="22" r="10"/><line x1="12" y1="22" x2="32" y2="22"/><line x1="22" y1="12" x2="22" y2="32"/><circle cx="5" cy="5" r="3"/><circle cx="39" cy="5" r="3"/><circle cx="5" cy="39" r="3"/><circle cx="39" cy="39" r="3"/></svg><div class="txt"><b>Infrastructure exposure:</b><br>IOT, code repos, cloud storage, pipelines &amp; more</div></div>
<div class="abs feature" style="top:2445px;background:#08c2ea"><svg width="44" height="44" viewBox="0 0 44 44" fill="none" stroke="#fff" stroke-width="1.6"><rect x="14" y="4" width="26" height="20"/><polyline points="17,20 24,13 30,17 37,8"/><circle cx="10" cy="26" r="5"/><path d="M2 42c0-8 4-11 8-11s8 3 8 11"/></svg><div class="txt"><b>People exposure</b><br>Social media monitoring</div></div>
<div class="abs feature" style="top:2517px;background:#14b7e2"><svg width="44" height="44" viewBox="0 0 44 44" fill="none" stroke="#fff" stroke-width="1.8"><circle cx="22" cy="22" r="18"/><circle cx="22" cy="22" r="6"/><line x1="22" y1="4" x2="22" y2="16"/><line x1="6" y1="31" x2="17" y2="25"/><line x1="38" y1="31" x2="27" y2="25"/></svg><div class="txt"><b>Ransomware exposure</b><br>leak &amp; credential monitoring</div></div>
<div class="abs feature" style="top:2589px;background:#4fd0ef"><svg width="44" height="44" viewBox="0 0 44 44" fill="none" stroke="#fff" stroke-width="1.6"><rect x="6" y="4" width="32" height="22"/><circle cx="22" cy="14" r="4"/><rect x="4" y="32" width="10" height="8"/><rect x="30" y="32" width="10" height="8"/><line x1="14" y1="36" x2="30" y2="36"/><line x1="22" y1="26" x2="22" y2="36"/></svg><div class="txt"><b>Attack prevention</b><br>Domain and certificate monitoring</div></div>

<!-- about -->
<section class="abs about" role="img" aria-label="Dark blue circuit board texture" style="background-image:linear-gradient(180deg,#0a1f3c 0%,#133663 55%,#0b2244 100%)"></section>
<h2 class="abs h2 light" style="left:0;width:1200px;text-align:center;top:2770px;font-size:26px">ABOUT VELTRANA</h2>
<div class="abs rule light" style="left:565px;top:2826px"></div>
<div class="abs about" style="background:none;top:2866px;height:auto"><p style="width:600px;margin:0 auto">Veltrana (company registration number CHE-418.902.117) was started in 2018 as a public limited company in Lenzhofen, Switzerland. Our analysts have long-standing relationships with various players on the Darknet. These personal relationships make it possible for Veltrana to repeatedly obtain the latest data leaks. Those unique data leaks are published by the press around the world.</p></div>

<!-- contact -->
<section class="abs contact" role="img" aria-label="Blue background with flowing digital light streams"></section>
<h2 class="abs h2 light" style="left:0;width:1200px;text-align:center;top:3097px">WANT TO KNOW MORE?</h2>
<div class="abs rule light" style="left:585px;top:3142px;width:30px"></div>
<div class="abs panel"></div>
<div class="abs field" style="left:331px;top:3216px;width:262px;height:44px">First Name</div>
<div class="abs field" style="left:607px;top:3216px;width:262px;height:44px">Last Name</div>
<div class="abs field" style="left:331px;top:3276px;width:262px;height:44px">Email</div>
<div class="abs field" style="left:607px;top:3276px;width:262px;height:44px">Phone</div>
<div class="abs field" style="left:331px;top:3334px;width:538px;height:128px">Message</div>
<div class="abs submit">SUBMIT</div>

<!-- footer -->
<div class="abs foot-brand">DOMAIN MONITORING</div>
<nav class="abs foot-nav">
  <span style="width:76px">HOME</span>
  <span style="width:122px">ABOUT US</span>
  <span style="width:108px">PROTECT</span>
  <span style="width:128px">CONTACT US</span>
</nav>
<div class="abs follow">FOLLOW US <span class="dot"></span><span class="dot alt"></span></div>
<div class="abs copy">© Veltrana.io - All rights reserved</div>

</body>
</html>
```